Brisbane IT support business needs our first website

Hi All,

We are after a new website design for our IT solutions and support business.The business name is Harlow Digital Systems Group, or HDSG for short. We provide a range of solutions and services within the IT space.

I would like to utilize the two colours in our business logo I have uploaded.

I understand this is initially for the design only aspect of the site, but I would like to engage the winner to finish coding the website and finalize after also.

Target Market(s)

Other businesses owners and home users.

Industry/Entity Type

Business

Requirements
Must have
• Nice clean and functional design utilizing our business colours from the logo.

```html
<!DOCTYPE html>
<html lang="en">
<head>
<meta charset="utf-8">
<title>Harlow Digital Systems Group</title>
<link href="https://fonts.googleapis.com/css2?family=Raleway:wght@400;500;600;700&family=Lato:ital,wght@0,400;0,700;1,400&display=swap" rel="stylesheet">
<style>
:root{
  --orange:#f07b1c;
  --orange-dark:#e2660e;
  --ink:#333333;
  --muted:#8a8a8a;
  --light:#f7f7f7;
  --line:#e3e3e3;
  --footer:#333333;
  --footer-deep:#2a2a2a;
  --footer-text:#b5b5b5;
  --green:#5cb85c;
}
*{box-sizing:border-box;margin:0;padding:0}
html,body{width:1000px;height:1200px;overflow:hidden;background:#fff}
body{position:relative;font-family:'Lato',sans-serif;color:var(--ink)}

/* header */
.site-header{position:absolute;left:145px;top:0;width:711px;height:43px;background:#fff}
.brand{position:absolute;left:15px;top:12px;font-family:'Raleway',sans-serif;font-weight:700;font-size:18px;color:var(--ink);letter-spacing:1px;line-height:1}
.main-nav{position:absolute;right:58px;top:17px;display:flex;gap:18px;font-family:'Raleway',sans-serif;font-weight:600;font-size:7.5px;letter-spacing:.8px}
.main-nav a{color:var(--ink);text-decoration:none}
.main-nav a.active{color:var(--orange)}
.nav-search{position:absolute;right:0;top:0;width:42px;height:43px;border-left:1px solid var(--line);display:flex;align-items:center;justify-content:center}

/* portfolio slider */
.portfolio{position:absolute;left:145px;top:43px;width:711px;height:278px;overflow:hidden}
.tile{position:absolute;overflow:hidden}
.tile-caption{position:absolute;left:8px;bottom:9px;color:#fff}
.tile-caption h3{font-family:'Raleway',sans-serif;font-weight:600;font-size:9.5px}
.tile-caption p{font-size:6.5px;opacity:.85;margin-top:2px}
.tile-nav{position:absolute;right:10px;bottom:12px;width:16px}
.tile-nav span{display:flex;width:16px;height:16px;background:rgba(40,40,40,.75);margin-top:2px;align-items:center;justify-content:center}
.slide-arrow{position:absolute;top:127px;width:18px;height:24px;background:rgba(0,0,0,.35);display:flex;align-items:center;justify-content:center}

/* features */
.feature{position:absolute;top:356px;width:150px;text-align:center}
.feature-icon{width:54px;height:54px;border-radius:50%;margin:0 auto;background:linear-gradient(135deg,var(--orange),var(--orange-dark));display:flex;align-items:center;justify-content:center}
.feature h4{margin-top:17px;font-family:'Raleway',sans-serif;font-weight:700;font-size:9px;letter-spacing:.8px;color:var(--ink)}
.feature p{margin-top:5px;font-family:'Raleway',sans-serif;font-size:9px;color:var(--muted);line-height:14px}

/* quote band */
.quote-band{position:absolute;left:145px;top:503px;width:711px;height:90px;background:var(--light);display:flex;align-items:center;justify-content:center}
.quote-band blockquote{font-family:'Raleway',sans-serif;font-weight:600;font-size:17px;letter-spacing:.6px;color:#2b2b2b}

/* partners & testimonial */
.section-title{position:absolute;top:629px;font-family:'Raleway',sans-serif;font-weight:500;font-size:10px;color:var(--ink)}
.partners{position:absolute;left:184px;top:659px;width:413px;height:138px;display:grid;grid-template-columns:repeat(5,1fr);grid-template-rows:1fr 1fr}
.partner{display:flex;align-items:center;justify-content:center;border-right:1px dashed var(--line);border-bottom:1px dashed var(--line)}
.partner:nth-child(5n){border-right:none}
.partner:nth-child(n+6){border-bottom:none}
.badge{background:#c9c9c9}
.testimonial{position:absolute;left:623px;top:659px;width:193px;height:104px;border:1px solid #ececec;box-shadow:0 1px 3px rgba(0,0,0,.08);background:#fff}
.avatar{position:absolute;left:11px;top:11px;width:36px;height:36px;border-radius:50%;background:linear-gradient(135deg,#d8c3b0,#8f7767)}
.testimonial blockquote{position:absolute;left:56px;top:13px;width:128px;font-style:italic;font-size:8px;line-height:13px;color:#555}
.testimonial cite{position:absolute;left:56px;top:73px;font-style:normal;font-family:'Raleway',sans-serif;font-weight:700;font-size:7px;color:#444}
.testimonial .company{position:absolute;left:61px;top:84px;font-size:6px;color:var(--muted)}
.dots{position:absolute;right:12px;top:85px;display:flex;gap:2px}
.dots i{width:4px;height:4px;border-radius:50%;background:#f4b27d}
.dots i:first-child{background:var(--orange)}

/* footer */
.site-footer{position:absolute;left:145px;top:841px;width:711px;height:279px;background:var(--footer);color:var(--footer-text);font-size:7.5px}
.foot-title{position:absolute;top:48px;font-family:'Raleway',sans-serif;font-weight:700;font-size:9px;letter-spacing:1.2px;color:#e6e6e6}
.foot-text{position:absolute;line-height:12px}
.foot-text strong{color:#e6e6e6}
.blogroll{position:absolute;left:182px;top:74px;list-style:none}
.blogroll li{height:16px;color:#d0d0d0}
.blogroll li::before{content:"›";margin-right:5px;color:#ccc}
.post{position:absolute;left:325px;width:125px;border-bottom:1px solid #444;padding-bottom:8px}
.post h5{font-weight:400;font-size:8px;line-height:12px;color:#e0e0e0}
.post time{display:block;font-style:italic;font-size:6px;color:var(--muted);margin-top:4px}
.stat{position:absolute;top:50px}
.stat b{display:block;font-family:'Raleway',sans-serif;font-weight:600;font-size:17px;color:#e8e8e8;letter-spacing:.5px}
.stat span{display:block;margin-top:6px;font-size:7px;letter-spacing:1px;color:#bdbdbd}
.to-top{position:absolute;width:22px;height:22px;background:#222;display:flex;align-items:center;justify-content:center}
.newsletter-text{position:absolute;left:478px;top:126px;width:195px;line-height:12px;color:#e6e6e6}
.newsletter-text strong{color:#fff}
.subscribe{position:absolute;left:478px;top:162px;width:193px;height:19px;display:flex}
.subscribe .send{width:20px;background:#1e1e1e;display:flex;align-items:center;justify-content:center}
.subscribe .field{flex:1;background:#262626;color:#777;font-size:7px;padding-left:6px;display:flex;align-items:center}
.subscribe .btn{width:48px;background:var(--green);color:#fff;font-size:7.5px;display:flex;align-items:center;justify-content:center}
.follow{position:absolute;top:207px;display:flex;gap:6px;align-items:center;font-size:6px;line-height:9px;color:#ddd}
.follow i{width:22px;height:22px;display:block}
.bottom-bar{position:absolute;left:145px;top:1120px;width:711px;height:80px;background:var(--footer-deep);color:#777;font-size:7.5px}
.bottom-bar .copy{position:absolute;left:39px;top:26px}
.bottom-bar .legal{position:absolute;left:39px;top:40px;border-bottom:1px solid #555;padding-bottom:3px}
.socials{position:absolute;left:517px;top:28px;display:flex;gap:10px}
.socials i{width:7px;height:7px;border-radius:50%;background:#666;display:block}
.contact-line{position:absolute;left:478px;top:46px;color:#8a8a8a}
</style>
</head>
<body>

<header class="site-header">
  <div class="brand">HDSG</div>
  <nav class="main-nav">
    <a class="active" href="#">HOME</a><a href="#">ABOUT</a><a href="#">PORTFOLIO</a><a href="#">BLOG</a><a href="#">FAQ</a><a href="#">CONTACT</a>
  </nav>
  <div class="nav-search">
    <svg width="9" height="9" viewBox="0 0 10 10"><circle cx="4" cy="4" r="3" fill="none" stroke="#333" stroke-width="1.5"/><line x1="6.3" y1="6.3" x2="9" y2="9" stroke="#333" stroke-width="1.6"/></svg>
  </div>
</header>

<section class="portfolio">
  <div class="tile" style="left:0;top:0;width:175px;height:278px;background:linear-gradient(160deg,#3fae8e 0%,#c9763a 45%,#d3426e 70%,#4a9a72 100%)" role="img" aria-label="Colourful abstract satellite-style terrain artwork">
    <div class="tile-caption"><h3>Graphic Designing</h3><p>Illustrations, Graphics</p></div>
  </div>
  <div class="tile" style="left:176px;top:0;width:175px;height:92px;background:linear-gradient(160deg,#6e6e6e,#2e2e2e)" role="img" aria-label="Open sketchbook with a coffee cup on a dark desk">
    <div class="tile-caption"><h3>Locked Steel Gate</h3><p>Illustrations</p></div>
  </div>
  <div class="tile" style="left:176px;top:93px;width:175px;height:92px;background:linear-gradient(160deg,#a9a9a9,#4a4a4a)" role="img" aria-label="Stationery set with letterhead, cards and pen">
    <div class="tile-caption"><h3>Slate Sunglasses</h3><p>Graphics, UI Elements</p></div>
  </div>
  <div class="tile" style="left:176px;top:186px;width:175px;height:92px;background:linear-gradient(160deg,#b08a72,#4d3b33)" role="img" aria-label="Stack of printed business cards on wood">
    <div class="tile-caption"><h3>Grotesque</h3><p>Illustrations, Graphics</p></div>
    <div class="tile-nav"><span><svg width="6" height="4"><path d="M0 4L3 1L6 4" fill="none" stroke="#fff"/></svg></span><span><svg width="6" height="4"><path d="M0 0L3 3L6 0" fill="none" stroke="#fff"/></svg></span></div>
  </div>
  <div class="tile" style="left:352px;top:0;width:173px;height:278px;background:linear-gradient(170deg,#8b8f96,#5b5e66 50%,#7a6a60)" role="img" aria-label="Collage of printed signs and election posters">
    <div class="tile-caption"><h3>Web Designing</h3><p>Motion, Web</p></div>
  </div>
  <div class="tile" style="left:526px;top:0;width:175px;height:138px;background:linear-gradient(135deg,#8fcab7,#e0c060 40%,#d9455c 70%,#6b6b6b)" role="img" aria-label="Colourful stacks of printed business cards">
    <div class="tile-caption"><h3>Study Table</h3><p>Graphics, Media</p></div>
  </div>
  <div class="tile" style="left:526px;top:139px;width:175px;height:139px;background:linear-gradient(160deg,#6a6158,#2c3642)" role="img" aria-label="Printed fabric pouch on a wooden table">
    <div class="tile-caption"><h3>Garden Sidebench</h3><p>Video</p></div>
    <div class="tile-nav"><span><svg width="6" height="4"><path d="M0 4L3 1L6 4" fill="none" stroke="#fff"/></svg></span><span><svg width="6" height="4"><path d="M0 0L3 3L6 0" fill="none" stroke="#fff"/></svg></span></div>
  </div>
  <div class="tile" style="left:702px;top:0;width:9px;height:278px;background:#5a534c" role="img" aria-label="Edge of next portfolio image"></div>
  <div class="slide-arrow" style="left:4px"><svg width="6" height="10"><path d="M5 1L1 5L5 9" fill="none" stroke="#fff" stroke-width="1.5"/></svg></div>
  <div class="slide-arrow" style="left:688px"><svg width="6" height="10"><path d="M1 1L5 5L1 9" fill="none" stroke="#fff" stroke-width="1.5"/></svg></div>
</section>

<section class="features">
  <div class="feature" style="left:179px">
    <div class="feature-icon"><svg width="22" height="20" viewBox="0 0 22 20" fill="none" stroke="#3a2410" stroke-width="1.5"><path d="M2 7L4 2H18L20 7Z"/><path d="M3 7V18H19V7"/><rect x="8" y="11" width="6" height="7"/></svg></div>
    <h4>E-COMMERCE SOLUTIONS</h4><p>Start your Own Shop today</p>
  </div>
  <div class="feature" style="left:343px">
    <div class="feature-icon"><svg width="22" height="18" viewBox="0 0 22 18" fill="none" stroke="#3a2410" stroke-width="1.5"><rect x="2" y="3" width="18" height="13" rx="2"/><path d="M13 8H20V12H13Z"/></svg></div>
    <h4>EASY PAYMENT OPTIONS</h4><p>Credit Cards &amp; Brimlet Pay<br>Support</p>
  </div>
  <div class="feature" style="left:507px">
    <div class="feature-icon"><svg width="22" height="20" viewBox="0 0 22 20" fill="none" stroke="#3a2410" stroke-width="1.5"><path d="M3 8H7L16 3V17L7 12H3Z"/><path d="M6 12L8 18"/><path d="M18 8V12"/></svg></div>
    <h4>INSTANT NOTIFICATIONS</h4><p>Realtime Email &amp; SMS<br>Support</p>
  </div>
  <div class="feature" style="left:672px">
    <div class="feature-icon"><svg width="18" height="22" viewBox="0 0 18 22" fill="none" stroke="#3a2410" stroke-width="1.5"><path d="M9 2C10 7 16 9 15 15A6 6 0 0 1 3 15C3 11 6 10 6 6C8 8 8 10 8 10C10 8 9 5 9 2Z"/></svg></div>
    <h4>HOT OFFERS DAILY</h4><p>Upto 50% Discounts</p>
  </div>
</section>

<section class="quote-band">
  <blockquote>"EVERYTHING IS DESIGNED, BUT SOME THINGS ARE DESIGNED WELL."</blockquote>
</section>

<h2 class="section-title" style="left:184px">Our Partners</h2>
<div class="partners">
  <div class="partner"><span class="badge" style="width:30px;height:34px;border-radius:4px 4px 15px 15px"></span></div>
  <div class="partner"><span class="badge" style="width:36px;height:36px;border-radius:50%;background:#e2e2e2"></span></div>
  <div class="partner"><span class="badge" style="width:46px;height:18px;border-radius:3px"></span></div>
  <div class="partner"><span class="badge" style="width:44px;height:30px;border-radius:2px;background:#d2d2d2"></span></div>
  <div class="partner"><span class="badge" style="width:48px;height:28px;border-radius:2px;background:#cfcfcf"></span></div>
  <div class="partner"><span class="badge" style="width:34px;height:34px;border-radius:50%"></span></div>
  <div class="partner"><span class="badge" style="width:46px;height:34px;border-radius:3px;background:#bdbdbd"></span></div>
  <div class="partner"><span class="badge" style="width:46px;height:32px;border-radius:50%;background:#d0d0d0"></span></div>
  <div class="partner"><span class="badge" style="width:48px;height:30px;border-radius:2px;background:#cfcfcf"></span></div>
  <div class="partner"><span class="badge" style="width:48px;height:24px;border-radius:12px;background:#d2d2d2"></span></div>
</div>

<h2 class="section-title" style="left:623px">What our Clients Say?</h2>
<div class="testimonial">
  <div class="avatar" role="img" aria-label="Client portrait photo"></div>
  <blockquote>"Similique fugit repellendus expedita excepturi iure perferendis provident quia eaque. Repellendus, vero numquam?"</blockquote>
  <cite>– DANA WHITLOW</cite>
  <span class="company">Corvane Ltd.</span>
  <div class="dots"><i></i><i></i><i></i></div>
</div>

<footer class="site-footer">
  <h3 class="foot-title" style="left:39px">ABOUT US</h3>
  <p class="foot-text" style="left:39px;top:73px;width:120px">We believe in <strong>Simple, Creative &amp; Flexible</strong> Design Standards.</p>
  <p class="foot-text" style="left:39px;top:121px;width:130px"><strong>Headquarters:</strong><br>48 Marlow Street, Level 3<br>Kelvin Grove, QLD 4059</p>
  <p class="foot-text" style="left:39px;top:170px;width:130px"><strong>Phone:</strong> (07) 5550 1842<br><strong>Fax:</strong> (07) 5550 1843<br><strong>Email:</strong> hello@hdsg.example</p>

  <h3 class="foot-title" style="left:182px">BLOGROLL</h3>
  <ul class="blogroll">
    <li>Documentation</li><li>Feedback</li><li>Plugins</li><li>Support Forums</li><li>Themes</li><li>PressKit Blog</li><li>PressKit Planet</li>
  </ul>

  <h3 class="foot-title" style="left:325px">RECENT POSTS</h3>
  <article class="post" style="top:73px"><h5>Lorem ipsum dolor sit amet, consectetur</h5><time>10th July 2014</time></article>
  <article class="post" style="top:138px"><h5>Elit Assumenda vel amet dolorum quasi</h5><time>10th July 2014</time></article>
  <article class="post" style="top:197px;border-bottom:none"><h5>Debitis nihil placeat, illum est nisi</h5><time>10th July 2014</time></article>

  <div class="stat" style="left:478px"><b>2,775,250</b><span>TOTAL VIEWS</span></div>
  <div class="stat" style="left:583px"><b>4,691</b><span>CLIENTS</span></div>
  <div class="to-top" style="left:672px;top:74px"><svg width="8" height="5"><path d="M1 4.5L4 1.5L7 4.5" fill="none" stroke="#fff" stroke-width="1.4"/></svg></div>

  <p class="newsletter-text"><strong>Subscribe</strong> to Our Newsletter to get Important News, Amazing Offers &amp; Inside Scoops:</p>
  <div class="subscribe">
    <span class="send"><svg width="8" height="8" viewBox="0 0 8 8"><path d="M0 4L8 0L5 8L4 5Z" fill="#aaa"/></svg></span>
    <span class="field">Enter your Email</span>
    <span class="btn">Subscribe</span>
  </div>
  <div class="follow" style="left:478px"><i style="background:#3b5a98"></i><span><b>Like us</b><br>on Friendspace</span></div>
  <div class="follow" style="left:583px"><i style="background:#f0782a"></i><span><b>Subscribe</b><br>to RSS Feeds</span></div>
</footer>

<div class="bottom-bar">
  <span class="copy">Copyrights © 2014 All Rights Reserved</span>
  <span class="legal">Terms of Use / Privacy Policy</span>
  <div class="socials"><i></i><i></i><i></i><i></i><i></i><i></i><i></i><i></i></div>
  <span class="contact-line">hello@hdsg.example · +61-7-5550-1844 · OnCallr</span>
  <div class="to-top" style="left:672px;top:42px"><svg width="8" height="5"><path d="M1 4.5L4 1.5L7 4.5" fill="none" stroke="#fff" stroke-width="1.4"/></svg></div>
</div>

</body>
</html>
```